Workvane Background Design

Need to develop a Workvane Background picture for my profile. The components I want in there are:
1) Name: Mohit Varma
2) Key Skills: Strategy, Innovation, Execution, Growth and Leadership
3) A photograph (an action photograph) The attached photograph is an example.
A black background would be ideal.

The design should meet the Workvane background size requirements.

The background should reinforce an image of a thinking person but equally capable of implementing.

Leadership

```html
<!DOCTYPE html>
<html lang="en">
<head>
<meta charset="utf-8">
<title>Mohit Varma – Workvane Background</title>
<link href="https://fonts.googleapis.com/css2?family=Courier+Prime:wght@700&family=Ubuntu:wght@700&display=swap" rel="stylesheet">
<style>
  :root {
    --bg: #000000;
    --skill-blue: #3aaee2;
    --name-blue: #35b2ec;
    --photo-dark: #1c1c22;
    --photo-mid: #4a4a52;
  }
  html, body {
    margin: 0;
    padding: 0;
    overflow: hidden;
    background: var(--bg);
  }
  .banner {
    position: relative;
    width: 1200px;
    height: 409px;
    background: var(--bg);
    overflow: hidden;
  }
  .skills {
    position: absolute;
    top: 4px;
    right: 819px;
    margin: 0;
    padding: 0;
    list-style: none;
    transform: scaleX(-1);
    text-align: left;
    font-family: "Courier Prime", "Courier New", monospace;
    font-weight: 700;
    font-size: 37px;
    line-height: 54px;
    color: var(--skill-blue);
  }
  .action-photo {
    position: absolute;
    left: 500px;
    top: 0;
    width: 375px;
    height: 409px;
    background: radial-gradient(ellipse at 50% 40%, var(--photo-mid) 0%, var(--photo-dark) 60%, var(--bg) 100%);
  }
  .name {
    position: absolute;
    left: 478px;
    top: 290px;
    margin: 0;
    font-family: "Ubuntu", "Verdana", sans-serif;
    font-weight: 700;
    font-size: 86px;
    line-height: 1;
    letter-spacing: 1px;
    color: var(--name-blue);
    white-space: nowrap;
  }
</style>
</head>
<body>
  <div class="banner">
    <ul class="skills">
      <li>strategy</li>
      <li>execution</li>
      <li>innovation</li>
      <li>growth</li>
      <li>leadership</li>
    </ul>
    <div class="action-photo" role="img" aria-label="Action photograph of Mohit Varma in a dark blazer and striped shirt, pointing upward while speaking"></div>
    <h1 class="name">Mohit VARMA</h1>
  </div>
</body>
</html>
```